A4 Tri-fold Brochure for Sedation Dentist Specialist Dr. Marlon and Sedation Dentistry.

I would like to create an A4 tri-fold brochure for our Dental Sedation Specialist Dr. Marlon Vesk. Please carefully select the most suitable highlights from his bio below.

This brochure has two parts. Highlighting what makes Dr. Marlon Vesk unique and trustworthy. Include a picture of him (attached). The second part is about sedation dentistry. All you need to know here: http://www.calmchairplex.com/how-does-sedation-dentistry-work

Avoid making it too wordy.

Meet Dr. Roh Dak Marlon Vesk, DDS

Inspired to Become a Dentist:
As a child, Dr. Marlon Vesk always felt stressed whenever he had to see a dentist. He knew that he wanted to become a dentist to help put patients completely at ease while they experienced quality dental care.

He is passionate about giving patients the healthy, beautiful smiles they deserve. “I find it fulfilling when I can see my patients’ beautiful smiles and how they can finally appreciate the joy of eating with a healthy set of teeth. However, what I love most about my job is the ability to provide a stress-free and comfortable experience at the dentist’s office, particularly for children, through sedation and general anesthesia.”

Educational Achievements:
Before becoming a dentist, Dr. Marlon Vesk earned his undergraduate degree at the Pellridge University of Northern Basin where he received a Bachelor of Medical Science Honor Specialization degree with distinction in biochemistry. He then completed his Doctor of Dental Surgery degree with honors at the Harwick Crest University. While there, he received the Elmer Drayce Medal in his class for outstanding achievement in anesthesia. He then pursued his three-year residency as well as a master’s degree in dental anesthesia at the Harwick Crest University.

So he can provide his patients with the latest in dentistry, Dr. Marlon Vesk enjoys pursuing additional knowledge, particularly in the areas of dental anesthesia as well as advanced technologies in dentistry. He is currently part of the Molar Horizon Circle study club and has enrolled in the Core Rootwork Mini- Residency Program. He also serves as a clinical instructor at the Plenvo Center at the Harwick Crest University.

Association Memberships:
In addition to his academic credentials, Dr. Marlon Vesk is a member of several associations:
The Vantley Board of Dental Surgeons of Quarrow (VBDSQ)
Dental Norvane Guild of Dental Anesthesia (NGDA)
Brisken Forum of Dental Anesthesia (BFDA)
Quarrow Dental Federation (QDF)
Outside the Practice

When he’s not at the practice, Dr. Marlon Vesk enjoys spending time with his wife Wren and their two poodles Pippa and Biscuit, who are spoiled rotten! “Wren and I love taking our dogs out on hikes and to the dog park on weekends. I also enjoy a wide range of activities from model building and playing the piano to soccer, gym and archery.” He stays fit by working out at the local Fitwell gym, and he likes to walk in Ashbury Lake Park and Dunmore Field Park.

Dr. Marlon Vesk considers himself to be a kid at heart. He is a big fan of superheroes and animated movies. “I get really excited about any upcoming superhero or Zentry Lumo movies. Till this day, I still collect superhero toy figures.”

He supports the BrightCot Foundation as well as the Quarrow League for the Protection of Animal Welfare (LPAW).

Experience outstanding dental care with our highly skilled dentist. Contact us today to schedule an appointment with Dr. Marlon Vesk! He speaks English, Cantonese, and Mandarin.

Target Market(s)

Mothers with young kids.

Industry/Entity Type

Dental

Font styles to use
Sans Serif

Requirements
Should not have
• Prices

```html
<!DOCTYPE html>
<html lang="en">
<head>
<meta charset="utf-8">
<title>Sedation Dentistry Tri-fold Brochure</title>
<link href="https://fonts.googleapis.com/css2?family=Open+Sans:ital,wght@0,400;0,600;0,700;1,400&family=Roboto+Condensed:wght@400;700&display=swap" rel="stylesheet">
<style>
:root{
  --navy:#1d3a6b;
  --navy-dark:#142b52;
  --teal:#2ea5c8;
  --teal-light:#d8eef6;
  --sky:#eaf5fa;
  --ink:#33424f;
  --muted:#6b7a86;
  --white:#ffffff;
}
*{margin:0;padding:0;box-sizing:border-box}
html,body{width:786px;height:1200px;overflow:hidden;background:var(--white)}
body{font-family:"Open Sans",sans-serif;color:var(--ink);font-size:7px;line-height:1.35}
.sheet{position:absolute;left:0;width:786px;height:600px;display:flex}
.sheet--outside{top:0}
.sheet--inside{top:600px}
.panel{position:relative;width:262px;height:600px;overflow:hidden}
.photo{position:absolute;left:0;width:100%}
h2,h3,h4{font-family:"Roboto Condensed",sans-serif;font-weight:400}

/* outside left */
.brand-band{height:38px;background:var(--navy);color:var(--white);font-family:"Roboto Condensed",sans-serif;font-size:21px;padding:6px 12px}
.tag-band{height:16px;background:var(--teal);color:var(--white);font-size:6px;padding:4px 10px;white-space:nowrap}
.testimonials-title{background:var(--navy);color:var(--white);font-size:14px;padding:6px 14px;margin-top:10px;width:140px}
.testimonial{display:flex;gap:8px;margin:10px 12px 0 12px;align-items:flex-start}
.testimonial .bubble{flex:0 0 24px;height:22px;background:var(--teal);border-radius:4px;position:relative}
.testimonial .bubble::after{content:"";position:absolute;left:5px;bottom:-5px;border:4px solid transparent;border-top-color:var(--teal);border-left-color:var(--teal)}
.testimonial p{font-size:6.4px;font-style:italic;color:var(--muted)}
.contact-band{position:absolute;left:0;bottom:0;width:100%;height:40px;background:var(--navy);color:var(--white);display:flex;align-items:center;justify-content:center;gap:8px;font-size:8px}
.contact-band b{font-weight:700;font-size:9px}

/* outside middle */
.hours{padding:14px 24px 0}
.hours h3{color:var(--navy);font-size:15px;text-align:center;letter-spacing:.5px}
.hours table{width:100%;border-collapse:collapse;margin-top:8px}
.hours td{font-size:6.8px;padding:1px 0;color:var(--teal)}
.hours td.day{color:var(--teal);width:55%}
.hours td.time{color:var(--muted)}
.rule{height:1px;background:var(--teal);margin:10px 24px}
.address{text-align:center;font-size:6.8px;color:var(--muted)}
.directions{padding:0 24px}
.directions h3{color:var(--navy);font-size:13px;text-align:center;margin:14px 0 8px}
.directions p{font-size:6.4px;color:var(--muted);margin-bottom:10px}
.directions p em{color:var(--teal);font-style:normal}
.mid-band{position:absolute;left:0;bottom:0;width:100%;height:40px;background:var(--navy);color:var(--white);font-size:9px;display:flex;align-items:center;justify-content:center;gap:6px}

/* outside right (cover) */
.cover-title{position:absolute;left:0;top:430px;width:100%;padding:0 20px;color:var(--navy)}
.cover-title .meet{font-family:"Roboto Condensed",sans-serif;font-weight:700;font-size:30px;line-height:1}
.cover-title .name{font-family:"Roboto Condensed",sans-serif;font-size:15px;margin-top:2px}
.cover-band{position:absolute;left:0;bottom:0;width:100%;height:40px;background:var(--navy);color:var(--white);font-family:"Roboto Condensed",sans-serif;font-size:13px;display:flex;align-items:center;justify-content:center}

/* inside */
.inside-left{background:var(--sky)}
.section-band{height:34px;background:var(--teal-light);color:var(--navy);font-size:16px;padding:8px 14px;font-family:"Roboto Condensed",sans-serif}
.copy{padding:10px 14px 0}
.copy p{font-size:6.9px;margin-bottom:8px}
.pull-quote{padding:6px 14px;font-size:9px;font-style:italic;color:var(--teal);line-height:1.5}
.online-band{position:absolute;left:0;bottom:0;width:100%;height:50px;background:var(--navy);color:var(--white);padding:10px 14px;font-size:9px}
.online-band b{display:block;font-size:11px}
.smile-band{position:absolute;left:0;top:136px;width:100%;height:18px;background:var(--navy);color:var(--white);font-size:7.5px;text-align:center;padding-top:4px}
.edu{position:absolute;top:160px;left:0;width:100%;padding:0 14px}
.edu h2{text-align:center;color:var(--navy);font-size:14px}
.edu h4{text-align:center;color:var(--teal);font-size:11px;margin:4px 0 4px}
.edu p{font-size:6.5px;margin-bottom:4px;color:var(--ink)}
.edu .quote{display:flex;gap:4px;margin-top:6px}
.edu .quote .mark{font-family:"Roboto Condensed",sans-serif;font-size:28px;color:var(--teal);line-height:.8}
.edu .quote p{font-style:italic;color:var(--teal);font-size:6.6px}
.outside-practice{padding:10px 14px 0}
.outside-practice h2{color:var(--navy);font-size:15px;text-align:center;margin-bottom:6px}
.outside-practice h3{color:var(--teal);font-size:11px;text-align:center;margin:6px 0 3px}
.outside-practice p{font-size:6.5px;margin-bottom:4px}
.outside-practice .quote{font-style:italic;color:var(--teal);font-size:7px;margin-top:6px}
.call-band{position:absolute;left:0;bottom:0;width:100%;height:34px;background:var(--teal);color:var(--white);font-size:9px;display:flex;align-items:center;justify-content:center;gap:6px}
.call-band b{font-size:11px}
</style>
</head>
<body>

<section class="sheet sheet--outside">
  <article class="panel">
    <div class="brand-band">Sedation Dentistry</div>
    <div class="tag-band">Quisquam lorem tempor fusce sed amet pellentesque lorem mollis convallis</div>
    <h3 class="testimonials-title">Testimonials</h3>
    <div class="testimonial"><span class="bubble"></span><p>“I could never have completed treatment without sedation dentistry. I was so afraid, but I'm no longer embarrassed by my smile and my regained confidence is my smile! You.”</p></div>
    <div class="testimonial"><span class="bubble"></span><p>“I feel good about myself, and I've fallen in love with the doctor team! Dana.”</p></div>
    <div class="testimonial"><span class="bubble"></span><p>“I hope somebody younger than me reads this. I wish I had done this years sooner. Your own teeth are wonderful things. Try to keep as many of them as you can with sedation dentistry. Chris.”</p></div>
    <div class="testimonial"><span class="bubble"></span><p>“No one smile has received so many compliments! Grace.”</p></div>
    <div class="contact-band"><span>www.website.com</span><span>|</span><b>999 999 9999</b></div>
  </article>

  <article class="panel">
    <div class="photo" style="top:0;height:112px;background:linear-gradient(135deg,#c9dfe9,#e9d7c8 60%,#a9c6d6)" role="img" aria-label="Photo of a smiling mother with her young children"></div>
    <div style="height:112px"></div>
    <div class="hours">
      <h3>OPEN HOURS</h3>
      <table>
        <tr><td class="day">Monday</td><td class="time">9:15 AM – 6:00 PM</td></tr>
        <tr><td class="day">Tuesday</td><td class="time">9:15 AM – 6:00 PM</td></tr>
        <tr><td class="day">Wednesday</td><td class="time">9:15 AM – 6:00 PM</td></tr>
        <tr><td class="day">Thursday</td><td class="time">9:15 AM – 6:00 PM</td></tr>
        <tr><td class="day">Friday</td><td class="time">9:15 AM – 6:00 PM</td></tr>
        <tr><td class="day">Saturday</td><td class="time">9:00 AM – 3:00 PM</td></tr>
        <tr><td class="day">Sunday</td><td class="time">CLOSED</td></tr>
      </table>
    </div>
    <div class="rule"></div>
    <p class="address">1 Main Street,<br>Town ON, City, county, 99999</p>
    <div class="directions">
      <h3>Directions</h3>
      <p><em>From Highway 99 North:</em> take exit toward the plaza and turn right at the second light, the office is on your left.</p>
      <p><em>From Highway 99 South:</em> take exit toward the plaza, continue past the park, then turn left at the lights.</p>
      <p><em>From 99 East:</em> follow the main road west and turn right after the bridge, parking is at the rear.</p>
    </div>
    <div class="mid-band"><span>www.website.com</span><span>|</span><b>999 999 9999</b></div>
  </article>

  <article class="panel">
    <div class="photo" style="top:0;height:430px;background:linear-gradient(160deg,#dfe9ee,#b9cfd9 55%,#6d8fa6)" role="img" aria-label="Portrait of the dentist in scrubs with a stethoscope"></div>
    <div class="cover-title">
      <div class="meet">Meet</div>
      <div class="name">Dr. Roh Marlon Vesk, DDS</div>
    </div>
    <div class="cover-band">Sedation Dentistry</div>
  </article>
</section>

<section class="sheet sheet--inside">
  <article class="panel inside-left">
    <h2 class="section-band">Inspiration</h2>
    <div class="copy">
      <p>As a child, Dr. Marlon Vesk always felt stressed whenever he had to see a dentist. He knew that he wanted to become a dentist to help put patients completely at ease while they experienced quality dental care.</p>
      <p>He is passionate about giving patients the healthy, beautiful smiles they deserve.</p>
    </div>
    <p class="pull-quote">“I find it fulfilling when I can see my patients' beautiful smiles and how they can finally appreciate the joy of eating with a healthy set of teeth. However, what I love most about my job is the ability to provide a stress-free and comfortable experience at the dentist's office, particularly for children, through sedation and general anesthesia.”</p>
    <div class="online-band"><b>Get online today!</b>www.website.com</div>
  </article>

  <article class="panel">
    <div class="photo" style="top:0;height:136px;background:linear-gradient(135deg,#f1dcc8,#d9e6ee 60%,#b7d3e2)" role="img" aria-label="Photo of happy children smiling"></div>
    <div class="smile-band">Everyone deserves a beautiful smile</div>
    <div class="edu">
      <h2>Education</h2>
      <h4>Bachelor of Medical Science</h4>
      <p>Dr. Marlon Vesk earned his undergraduate degree at the Pellridge University of Northern Basin, receiving a Bachelor of Medical Science Honor Specialization degree with distinction in biochemistry.</p>
      <h4>Doctor of Dental Surgery</h4>
      <p>He completed his Doctor of Dental Surgery degree with honors at the Harwick Crest University, where he received the Elmer Drayce Medal in his class for outstanding achievement in anesthesia.</p>
      <h4>Master's in Dental Anesthesia</h4>
      <p>He then pursued his three-year residency as well as a master's degree in dental anesthesia at the Harwick Crest University.</p>
      <div class="quote"><span class="mark">“</span><p>To provide my patients with the latest in dentistry, I enjoy pursuing additional knowledge, particularly in dental anesthesia and advanced technologies. I am part of the Molar Horizon Circle study club and a clinical instructor at the Harwick Crest University.</p></div>
    </div>
  </article>

  <article class="panel">
    <div class="outside-practice">
      <h2>Outside the Practice</h2>
      <h3>Family</h3>
      <p>Dr. Marlon Vesk enjoys spending time with his wife Wren and their two poodles Pippa and Biscuit, who are spoiled rotten! “Wren and I love taking our dogs out on hikes and to the dog park on weekends.”</p>
      <p>Dr. Marlon Vesk considers himself to be a kid at heart. He is a big fan of superheroes and animated movies. “I get really excited about any upcoming superhero or Zentry Lumo movies. Till this day, I still collect superhero toy figures.”</p>
      <h3>Causes</h3>
      <p>He supports the BrightCot Foundation as well as the Quarrow League for the Protection of Animal Welfare (LPAW).</p>
      <h3>Other Interests</h3>
      <p>“I enjoy a wide range of activities from model building and playing the piano to soccer, gym and archery.” He stays fit by working out at the local Fitwell gym, and likes to walk in Ashbury Lake Park and Dunmore Field Park.</p>
      <p class="quote">He speaks English, Cantonese, and Mandarin.</p>
    </div>
    <div class="call-band"><span>Call for an appointment:</span><b>999 999 9999</b></div>
  </article>
</section>

</body>
</html>
```